General brochure with course listing

A general brochure for the Global Statute Academy, about 40 A5 pages that includes mission, vision, history, descriptions of our technical assistance and capacity building programming and detailed descriptions of our courses. Would be for both online pdf (magazine style) and print. I have attached an example of an older one that was satisfactory but not as professional as what we're looking for now.

Target Market(s)

Lawyers and government officials around the world.

Industry/Entity Type

Legal and capacity building

Requirements
Must have
• A good design and template that we can replicate on our own in InDesign annually. We need the layout from you and we will provide the copy. We will also publish as a pdf
Nice to have
• Colors and branding from our website - www.gsa-learn.org

```html
<!DOCTYPE html>
<html lang="en">
<head>
<meta charset="utf-8">
<title>Global Statute Academy — Mission, Vision, History</title>
<link rel="stylesheet" href="https://fonts.googleapis.com/css2?family=Orbitron:wght@800&family=Sorts+Mill+Goudy&family=Crimson+Pro:wght@600&display=swap">
<style>
  :root {
    --coral: #ff6a65;
    --mist: #eff5f5;
    --navy: #0d1a80;
    --ink: #3a3f4a;
    --paper: #ffffff;
  }
  * { margin: 0; padding: 0; box-sizing: border-box; }
  html, body { width: 846px; height: 1200px; overflow: hidden; background: var(--paper); }
  .page { position: relative; width: 846px; height: 1200px; background: var(--paper); }

  .brand {
    position: absolute; left: 28px; top: 36px; width: 130px;
    font-family: "Sorts Mill Goudy", serif; color: var(--navy);
    font-size: 19px; line-height: 22px;
  }

  .accent-band { position: absolute; background: var(--coral); }
  .accent-band--top { left: 186px; top: 24px; width: 651px; height: 381px; }
  .accent-band--bottom { left: 23px; top: 694px; width: 430px; height: 188px; }

  .photo { position: absolute; }
  .photo--classroom { left: 49px; top: 140px; width: 434px; height: 401px;
    background: linear-gradient(135deg, #6b6a55 0%, #3b3b34 45%, #8a8470 100%); }
  .photo--market { left: 49px; top: 652px; width: 434px; height: 205px;
    background: linear-gradient(100deg, #e9e3e6 0%, #c9556b 40%, #3a2a3a 70%, #e2703e 100%); }

  .statement {
    position: absolute; left: 378px; width: 424px; background: var(--mist);
    padding: 31px 16px 0 38px;
  }
  .statement--mission { top: 62px; height: 391px; }
  .statement--vision { top: 574px; height: 197px; }

  .point {
    position: relative; list-style: none; padding-left: 0;
    font-family: "Sorts Mill Goudy", serif; font-size: 19px; line-height: 27px;
    color: #3d4048; margin-bottom: 27px;
  }
  .point svg { position: absolute; left: -31px; top: 4px; width: 18px; height: 18px; }

  .section-title {
    position: absolute; font-family: "Orbitron", sans-serif; font-weight: 800;
    color: var(--navy); line-height: 1; letter-spacing: 0.5px;
  }
  .section-title--mission { left: 505px; top: 479px; font-size: 50px; }
  .section-title--vision { left: 50px; top: 571px; font-size: 52px; }
  .section-title--history { left: 538px; top: 797px; font-size: 52px; }

  .history {
    position: absolute; left: 51px; top: 902px; width: 756px;
    font-family: "Crimson Pro", serif; font-weight: 600; font-size: 11.4px;
    line-height: 19.6px; color: var(--ink);
  }
  .history p { margin-bottom: 17px; }
</style>
</head>
<body>
<div class="page">
  <div class="brand">Global<br>Statute<br>Academy</div>

  <div class="accent-band accent-band--top"></div>
  <div class="accent-band accent-band--bottom"></div>

  <div class="photo photo--classroom" role="img" aria-label="Photo of an instructor presenting at a flip chart to participants seated around a seminar table in a law library"></div>
  <div class="photo photo--market" role="img" aria-label="Photo of a smiling entrepreneur standing beside her market stall of colourful textiles and crafts"></div>

  <ul class="statement statement--mission">
    <li class="point"><svg viewBox="0 0 18 18" aria-hidden="true"><circle cx="9" cy="9" r="9" fill="var(--coral)"/><path d="M7 5l4 4-4 4" fill="none" stroke="#fff" stroke-width="2.4" stroke-linecap="round" stroke-linejoin="round"/></svg>To be a global leader in delivering international law capacity-building, legal best practice certifications, and technical assistance programs worldwide.</li>
    <li class="point"><svg viewBox="0 0 18 18" aria-hidden="true"><circle cx="9" cy="9" r="9" fill="var(--coral)"/><path d="M7 5l4 4-4 4" fill="none" stroke="#fff" stroke-width="2.4" stroke-linecap="round" stroke-linejoin="round"/></svg>To communicate the benefits of the rules-based international system to institutions, lawyers and entrepreneurs worldwide.</li>
    <li class="point"><svg viewBox="0 0 18 18" aria-hidden="true"><circle cx="9" cy="9" r="9" fill="var(--coral)"/><path d="M7 5l4 4-4 4" fill="none" stroke="#fff" stroke-width="2.4" stroke-linecap="round" stroke-linejoin="round"/></svg>To collaborate with international and regional organizations to develop, implement and build capacity for international legal standards.</li>
  </ul>

  <h2 class="section-title section-title--mission">Mission</h2>
  <h2 class="section-title section-title--vision">vision</h2>

  <ul class="statement statement--vision">
    <li class="point"><svg viewBox="0 0 18 18" aria-hidden="true"><circle cx="9" cy="9" r="9" fill="var(--coral)"/><path d="M7 5l4 4-4 4" fill="none" stroke="#fff" stroke-width="2.4" stroke-linecap="round" stroke-linejoin="round"/></svg>To foster prosperity and human development for all through the rule of law.</li>
    <li class="point"><svg viewBox="0 0 18 18" aria-hidden="true"><circle cx="9" cy="9" r="9" fill="var(--coral)"/><path d="M7 5l4 4-4 4" fill="none" stroke="#fff" stroke-width="2.4" stroke-linecap="round" stroke-linejoin="round"/></svg>To de-risk sustainable development in order to advance the Sustainable Development Goals.</li>
  </ul>

  <h2 class="section-title section-title--history">History</h2>

  <div class="history">
    <p>GSA was founded in 1955 at the Harwick University Law Center to assist in rebuilding government and economic institutions, as well as the legal and institutional frameworks for infrastructure in post-war Europe. A sister institute, the Institut für Vergleichendes Handelsrecht, was founded at the same time in Frankfurt, Germany. Professor Heinrich Albrecht, the Institute’s first director, fled Germany in the 1930s and spent more than a decade studying and teaching at the law schools of Linden University and Harwick University. Professor Albrecht believed that closer ties between European and American legal systems would facilitate business and trade.</p>
    <p>The Institute’s early years were marked by scholarly work and academic exchanges. Beginning in the early 1970s – under the leadership of a new director, Professor Daniel Whitmore, Jr., of Harwick University – the GSA expanded its focus to include professional training in the legal, economic, and financial problems of developing countries. An early collaborator in this work was Professor Robert Halstead of Linden University Law School.</p>
    <p>The earliest courses offered were Foreign Investment Negotiation and International Procurement. Since then, the curriculum has evolved to reflect, and promote, the centrality of the private sector and an enabling role on the part of the public sector in promoting the conditions for economic growth.</p>
    <p>GSA became an independent, 501(c)(3) non-profit organization in 1983.&nbsp; It continues to work closely with universities, governments, corporations and international organizations.</p>
  </div>
</div>
</body>
</html>
```